Brightwell Renal Partners Brochure - Marketing brochure for a dialysis company in the USA

I want a brochure to be created for my business. I have a brochure that can be used as a comparison. My old Company name is Lone Mesa Renal Services. The new Company Name is Brightwell Renal Partners. I have a sample of the Old Brochure. and I uploaded the Logo of BRP. It will be used by my sales agents to introduce my company to potential client hospitals.

Target Market(s)

CEOs of Acute Hospitals and Medical Centers

Industry/Entity Type

Health Care

Requirements
Must have
• Use the sample as a guide. This project is for a 4 page brochure. (2 letter size pages folded in half crosswise) Use the text from the old brochure to the new brochure, replacing the old info with the new company info as needed.
Nice to have
• Here is my company info:
• Brightwell Renal Partners
• 4120 W 17th St
• Suite D
• It will be nice if the designer can give me the project files that would allow me to edit the text of the brochure.
• McAllen, TX 78519
• (956) 471-2283
• admin@BrightwellRenalLLC.com
• www.brightwellrenal.com

```html
<!DOCTYPE html>
<html lang="en">
<head>
<meta charset="utf-8">
<title>Brightwell Renal Partners Brochure</title>
<link href="https://fonts.googleapis.com/css2?family=PT+Sans:wght@400;700&family=PT+Sans+Narrow:wght@700&display=swap" rel="stylesheet">
<style>
  :root {
    --backdrop: #e4e5e8;
    --paper: #ffffff;
    --navy: #1f2a7a;
    --accent-red: #c8202f;
    --text: #333338;
    --panel: #e3e4e8;
  }
  * { box-sizing: border-box; margin: 0; padding: 0; }
  html, body { width: 1200px; height: 1200px; overflow: hidden; }
  body {
    background: var(--backdrop);
    font-family: "PT Sans", Arial, sans-serif;
    color: var(--text);
    position: relative;
  }
  .spread {
    position: absolute;
    left: 244px;
    width: 712px;
    height: 550px;
    background: var(--paper);
    box-shadow: 0 2px 8px rgba(0,0,0,.18);
  }
  .spread--first { top: 30px; }
  .spread--second { top: 620px; }
  .spread__header { position: absolute; left: 0; top: 0; width: 712px; height: 70px; }
  .brand { position: absolute; top: 42px; color: var(--navy); font-weight: 700; line-height: 1; }
  .brand__name { display: block; font-size: 30px; letter-spacing: -1px; }
  .brand__sub { display: block; font-size: 5.6px; letter-spacing: .2px; text-transform: uppercase; margin-top: 1px; }
  .brand--left { left: 32px; }
  .brand--right { right: 32px; }

  .block { position: absolute; font-size: 7px; line-height: 1.38; text-align: justify; }
  .block h3 {
    font-family: "PT Sans Narrow", "Arial Narrow", sans-serif;
    font-size: 8.2px; color: var(--navy); line-height: 1.3; margin-bottom: 5px; text-align: left;
  }
  .block--narrow { text-align: left; }
  .block p + p { margin-top: 7px; }

  .points { list-style: none; }
  .points li { position: relative; padding-left: 19px; margin-bottom: 10px; }
  .points li span.num {
    position: absolute; left: 0; top: 2px; width: 12px; height: 12px; border-radius: 50%;
    background: var(--accent-red); color: #fff; font-size: 6px; text-align: center; line-height: 12px;
  }
  .hl { color: var(--accent-red); font-weight: 700; }

  .photo { position: absolute; border: 1px solid var(--navy); }
  .photo--lab { background: linear-gradient(135deg, #6f88c4, #c9d3ea 55%, #b2463f); }
  .photo--machine { background: linear-gradient(160deg, #f4f6fa, #c9d6e6); }
  .photo--unit { border: none; background: linear-gradient(180deg, #eef2f7 0%, #dfe6ef 55%, #6fa2d8 100%); }
  .photo--screen { background: linear-gradient(135deg, #dde5ec, #9fb6c6 60%, #5e7d96); }
  .photo--bags { background: linear-gradient(135deg, #f2f4f8, #7aa0d6 60%, #e9c9b5); }
  .photo--procedure { background: linear-gradient(135deg, #9ab4dc, #e6dbd4 55%, #c14d55); }
  .photo--ward { background: linear-gradient(160deg, #b9d6ef, #5f93c9); }
  .photo--arm { border: none; background: linear-gradient(135deg, #d9d9d9, #d8a583 55%, #8e2b2b); }

  .panel { position: absolute; background: var(--panel); padding: 7px 9px; font-size: 7px; line-height: 1.38; }
  .panel h3 { font-family: "PT Sans Narrow", "Arial Narrow", sans-serif; font-size: 8.2px; color: var(--navy); line-height: 1.3; margin-bottom: 5px; }

  .footer-rule { position: absolute; left: 0; top: 510px; width: 712px; height: 3px; background: var(--accent-red); }
  .page-num {
    position: absolute; top: 516px; width: 24px; height: 20px; background: var(--accent-red);
    color: #fff; font-size: 8px; font-family: Arial, Helvetica, sans-serif; text-align: center; line-height: 20px;
  }
  .page-num--left { left: 26px; }
  .page-num--right { right: 26px; }
  .footer-url { position: absolute; top: 522px; font-size: 6.4px; letter-spacing: .8px; color: #333; }
  .footer-url--left { left: 238px; }
  .footer-url--right { left: 382px; }
</style>
</head>
<body>

<section class="spread spread--first">
  <svg class="spread__header" viewBox="0 0 712 70">
    <defs>
      <linearGradient id="bandA" x1="0" y1="0" x2="1" y2="0">
        <stop offset="0" stop-color="#2a3c9c"/><stop offset=".5" stop-color="#16206a"/><stop offset="1" stop-color="#2a3c9c"/>
      </linearGradient>
    </defs>
    <rect width="712" height="70" fill="url(#bandA)"/>
    <rect x="250" y="0" width="212" height="62" fill="#6f8fd0" opacity=".55" role="img" aria-label="Close-up photo of dialysis tubing and equipment"/>
    <path d="M0,36 Q180,34 330,56 L356,64 L382,56 Q532,34 712,36 L712,70 L0,70 Z" fill="#fff"/>
    <path d="M0,36 Q180,34 330,56 L356,64 L382,56 Q532,34 712,36" fill="none" stroke="#c8202f" stroke-width="3"/>
    <path d="M0,33 Q180,31 330,52 L356,60 L382,52 Q532,31 712,33" fill="none" stroke="#e8683a" stroke-width="1.2"/>
  </svg>

  <div class="brand brand--left"><span class="brand__name">BRP</span><span class="brand__sub">Brightwell Renal Partners</span></div>
  <div class="brand brand--right"><span class="brand__name">BRP</span><span class="brand__sub">Brightwell Renal Partners</span></div>

  <div class="block" style="left:32px; top:94px; width:292px;">
    <ol class="points">
      <li><span class="num">7</span>Our contracts are very flexible, so you have the ability to contract for only those services that your facility needs. If you have a need for hemodialysis only, we will tailor your contract to suit your needs. If, in the future, you wish to add other services, a contract addendum can be completed quickly.</li>
      <li><span class="num">8</span>Patient satisfaction is our top priority. If a patient is happy with our inpatient dialysis services, that patient will probably return to your facility when future medical services are needed. Thus, both of us will benefit from future revenue generated by that patient's return to your facility. We actually do patient satisfaction surveys, and act upon the results. Our competition does not do this.</li>
      <li><span class="num">9</span>We strive to cater to the needs of the nephrologist. We realize that nephrologists are a key driver of hospital inpatient dialysis volume. As such, we seek to cater to their needs.</li>
      <li><span class="num">10</span>Our management is very familiar with the JCAHO and TOH survey process, and we provide full support during JCAHO and TOH surveys. A member of our top management will be on site during these surveys to answer any questions the surveyor may have.</li>
      <li><span class="num">11</span>Any dialysis company can pass a JCAHO or TOH inspection when they know a week or two in advance that these surveyors are coming. In this era of drop-in JCAHO inspections, you need an inpatient dialysis provider that is always ready for inspection without advance notice. We strive to be survey ready 365 days per year.</li>
      <li><span class="num">12</span>The BRP education department is very familiar with the JCAHO and TOH requirements for staff credentialing and competencies, and strives to ensure that each of our staff members is JCAHO and TOH compliant at all times. In addition, BRP staff receives annual retraining in such areas as fire safety, infection control, and HIPAA compliance.</li>
    </ol>
  </div>

  <div class="photo photo--lab" style="left:32px; top:408px; width:104px; height:77px;" role="img" aria-label="Photo of a technician in protective clothing working in a laboratory"></div>
  <div class="panel" style="left:142px; top:408px; width:182px; height:77px;">
    <h3>How can I find out more about BRP and its services?</h3>
    <p>We're glad you asked! Call us anytime, 24 hours a day, 7 days a week at <span class="hl">+1.9564712283</span> extension <span class="hl">2</span>. We will be happy to provide you with a free, no obligations proposal for inpatient dialysis and related services.</p>
  </div>

  <div class="block" style="left:388px; top:106px; width:292px;">
    <h3>How does an acute inpatient dialysis contract work?</h3>
    <p>If you decide to contract with us, we provide all the dialysis staff, dialysis specific machines, dialysis water treatment system, dialysis specific supplies, dialysis specific biomedical services, dialysis specific paperwork, dialysis specific policies and procedures, and JCAHO required competencies and credentialing for our staff --all for one flat fee per treatment.</p>
    <p>When the nephrologist writes a treatment order, BRP staff perform that treatment according to the nephrologist's exact specifications. Dialysis treatments can be performed either at the bedside or in a separate dialysis room.</p>
  </div>

  <div class="photo photo--machine" style="left:390px; top:210px; width:93px; height:56px;" role="img" aria-label="Photo of a compact dialysis machine"></div>
  <div class="panel" style="left:488px; top:210px; width:192px; height:56px;">
    <h3>Does BRP have satisfied customers who can provide references?</h3>
    <p>Yes. We will be more than happy to provide you with a list of satisfied customers and nephrologists.</p>
  </div>

  <div class="block block--narrow" style="left:388px; top:282px; width:156px;">
    <h3>Who are BRP's competitors?</h3>
    <p>Two large dialysis companies, based in Massachusetts and California, provide most of the chronic outpatient and acute inpatient dialysis in the United States. In many locations, one of these two companies is the only dialysis provider in town, and can charge their hospital clients outrageous prices for acute inpatient dialysis services. The business focus of these two companies is roughly 95% chronic outpatient dialysis and 5% acute inpatient dialysis, so their focus is DEFINITELY NOT inpatient dialysis services.</p>
    <p>Since CMS reimbursement is very meager for chronic outpatient dialysis services, the profitability of a typical dialysis clinic is only about 5% at best. By adding inpatient dialysis to its menu of services, a dialysis outpatient clinic can boost its profitability by several percentage points at your expense.</p>
  </div>

  <div class="photo photo--unit" style="left:564px; top:282px; width:96px; height:220px;" role="img" aria-label="Photo of a tall white and blue apheresis unit with hanging fluid bags"></div>

  <div class="footer-rule"></div>
  <div class="page-num page-num--left">04</div>
  <div class="page-num page-num--right">05</div>
  <div class="footer-url footer-url--left">www.brightwellrenal.com</div>
  <div class="footer-url footer-url--right">www.brightwellrenal.com</div>
</section>

<section class="spread spread--second">
  <svg class="spread__header" viewBox="0 0 712 70">
    <defs>
      <linearGradient id="bandB" x1="0" y1="0" x2="1" y2="0">
        <stop offset="0" stop-color="#2a3c9c"/><stop offset=".5" stop-color="#16206a"/><stop offset="1" stop-color="#2a3c9c"/>
      </linearGradient>
    </defs>
    <rect width="712" height="70" fill="url(#bandB)"/>
    <rect x="250" y="0" width="212" height="62" fill="#6f8fd0" opacity=".55" role="img" aria-label="Close-up photo of dialysis tubing and equipment"/>
    <path d="M0,36 Q180,34 330,56 L356,64 L382,56 Q532,34 712,36 L712,70 L0,70 Z" fill="#fff"/>
    <path d="M0,36 Q180,34 330,56 L356,64 L382,56 Q532,34 712,36" fill="none" stroke="#c8202f" stroke-width="3"/>
    <path d="M0,33 Q180,31 330,52 L356,60 L382,52 Q532,31 712,33" fill="none" stroke="#e8683a" stroke-width="1.2"/>
  </svg>

  <div class="brand brand--left"><span class="brand__name">BRP</span><span class="brand__sub">Brightwell Renal Partners</span></div>
  <div class="brand brand--right"><span class="brand__name">BRP</span><span class="brand__sub">Brightwell Renal Partners</span></div>

  <div class="block block--narrow" style="left:31px; top:100px; width:140px;">
    <h3>Why are BRP's prices so low in comparison to the competition?</h3>
    <p>We do a huge volume of inpatient dialysis treatments, which allows us to purchase large quantities of supplies at lower prices. Unlike our competition, we don't have fifteen layers of management and millions of shareholders to support. In addition, our innovative staff compensation programs, and low turnover help keep our costs low.</p>
  </div>
  <div class="block block--narrow" style="left:31px; top:236px; width:140px;">
    <h3>What are the qualifications of the BRP staff?</h3>
    <p>Our staff is experienced in inpatient dialysis and related services. BRP staff are BCLS certified, and can be ACLS certified by our education department on request. All LMRS staff receive comprehensive pre-hire drug testing and background checks.</p>
  </div>
  <div class="block block--narrow" style="left:31px; top:366px; width:140px;">
    <h3>Does BRP employ a biomedical staff to maintain its equipment?</h3>
    <p>Yes. We have a full time, fully trained and credentialed biomedical staff. Copies of our machine maintenance and repair records are kept on site at your facility for compliance purposes. Like our dialysis staff, our biomedical staff is available 24 hours a day, 7 days a week.</p>
  </div>

  <div class="block block--narrow" style="left:179px; top:100px; width:138px;">
    <h3>Does BRP charge "add-on" fees for after-hours, weekend, callback, or holiday treatments?</h3>
    <p>No. We charge one flat fee per inpatient dialysis treatment, regardless of when it is performed.</p>
  </div>
  <div class="photo photo--screen" style="left:179px; top:173px; width:138px; height:105px;" role="img" aria-label="Photo of a dialysis machine touchscreen panel"></div>
  <div class="block block--narrow" style="left:179px; top:287px; width:138px;">
    <h3>Is BRP staff available for STAT, on-call, and after-hours treatments?</h3>
    <p>Yes. Part of our commitment to your facility involves being on-call to perform inpatient dialysis treatments 24 hours a day, 7 days a week.</p>
  </div>
  <div class="photo photo--bags" style="left:179px; top:370px; width:138px; height:106px;" role="img" aria-label="Photo of a gloved hand handling blood sample tubes"></div>

  <div class="block block--narrow" style="left:381px; top:100px; width:138px;">
    <h3>Is BRP insured?</h3>
    <p>Yes. BRP maintains comprehensive malpractice, workers' compensation, and employee health insurance coverage.</p>
    <h3 style="margin-top:10px;">Does BRP offer therapeutic apheresis.</h3>
    <p>Yes. One of the most exciting new therapies available to treat autoimmune diseases is therapeutic apheresis, and BRP is at the forefront of delivering these specialized treatments. BRP utilizes state-of-the-art Veltra equipment to perform cell separation therapy in the treatment of a wide range of diseases, including myasthenia gravis, Guillain-Barre syndrome, and thrombotic thrombocytopenia purpura (TTP). BRP offers therapeutic apheresis on the same 24/7/365 basis as our inpatient dialysis services, including weekends and holidays.</p>
    <p>Other providers not rooted in rapid-response, around-the-clock service tend to prefer the Monday through Friday, normal business hours type of service. Often, our hospital clients' patients need us during other than normal business hours, and we respond accordingly.</p>
  </div>

  <div class="block block--narrow" style="left:529px; top:100px; width:142px;">
    <h3>What CQI/QA support does BRP provide?</h3>
    <p>We provide monthly inpatient dialysis specific CQI/QA in full collaboration with your infection control department and other departments/committees. We also provide monthly water culture and LAL testing of our equipment, and yearly AAMI testing of our equipment.</p>
  </div>
  <div class="photo photo--procedure" style="left:529px; top:196px; width:142px; height:84px;" role="img" aria-label="Photo of gloved hands placing a catheter during a procedure"></div>
  <div class="photo photo--ward" style="left:529px; top:287px; width:142px; height:88px;" role="img" aria-label="Photo of a hospital intensive care room with a bed and monitors"></div>

  <div class="photo photo--arm" style="left:381px; top:381px; width:130px; height:102px;" role="img" aria-label="Photo of a needle and tubing in a patient's forearm"></div>
  <div class="panel" style="left:516px; top:383px; width:155px; height:106px;">
    <h3>If our facility agrees to contract with BRP for inpatient dialysis and related services, how quickly can the transition from our current dialysis provider to BRP be completed?</h3>
    <p>The transition can occur overnight in many cases. We have a dedicated transition team that takes care of these situations so that your facility never experiences a lapse in inpatient dialysis coverage.</p>
  </div>

  <div class="footer-rule"></div>
  <div class="page-num page-num--left">06</div>
  <div class="page-num page-num--right">08</div>
  <div class="footer-url footer-url--left">www.brightwellrenal.com</div>
  <div class="footer-url footer-url--right">www.brightwellrenal.com</div>
</section>

</body>
</html>
```